Business Card Design - Local Discount Club

Looking for a fun business card for a local discount club. One side should be the logo only and the other should be have :

Name
Title
Phone, Email
Website

```html
<!DOCTYPE html>
<html lang="en">
<head>
<meta charset="utf-8">
<title>Harbor Saver Club – Business Card</title>
<link rel="stylesheet" href="https://fonts.googleapis.com/css2?family=Lato:wght@400;900&family=Montserrat:wght@700&display=swap">
<style>
  :root {
    --bg: #2a2a2c;
    --card-blue: #3a5bbf;
    --card-blue-light: #5a78cf;
    --white: #ffffff;
    --cyan: #3fd4f5;
    --lime: #8ef07a;
    --text-light: #f2f5ff;
  }
  * { box-sizing: border-box; margin: 0; padding: 0; }
  html, body {
    width: 1200px; height: 1015px; overflow: hidden;
    background: var(--bg);
    font-family: "Lato", Arial, sans-serif;
  }
  .canvas {
    width: 1200px; height: 1015px;
    display: flex; flex-direction: column; align-items: center; justify-content: center;
    gap: 60px;
  }
  .card {
    position: relative;
    width: 640px; height: 366px;
    border-radius: 4px;
    overflow: hidden;
    box-shadow: 0 18px 40px rgba(0,0,0,.55);
  }
  .card-pattern {
    position: absolute; inset: 0;
    background:
      radial-gradient(circle at 20% 30%, var(--card-blue-light) 0, transparent 28%),
      radial-gradient(circle at 75% 75%, var(--card-blue-light) 0, transparent 30%),
      radial-gradient(circle at 55% 10%, var(--card-blue-light) 0, transparent 22%),
      var(--card-blue);
  }
  .brand-dot {
    width: 20px; height: 20px; border-radius: 50%;
    background: var(--white); flex: none;
  }
  .brand-name {
    font-family: "Montserrat", Arial, sans-serif;
    font-weight: 700;
    text-transform: uppercase;
    color: var(--white);
    line-height: 1.15;
  }
  /* Front: logo only */
  .front .brand {
    position: absolute; inset: 0;
    display: flex; align-items: center; justify-content: center; gap: 14px;
  }
  .front .brand-name { font-size: 34px; letter-spacing: 1px; }

  /* Back: details */
  .logo-disc {
    position: absolute;
    width: 400px; height: 400px;
    left: 320px; top: -80px;
    border-radius: 50%;
    background: var(--white);
    box-shadow: -7px 5px 0 0 var(--cyan);
  }
  .back .brand {
    position: absolute;
    left: 350px; right: 20px; top: 80px; height: 80px;
    display: flex; align-items: center; justify-content: center; gap: 12px;
  }
  .back .brand-dot { background: var(--card-blue); width: 16px; height: 16px; }
  .back .brand-name { color: var(--card-blue); font-size: 24px; letter-spacing: .5px; }

  .identity {
    position: absolute; left: 44px; top: 80px;
  }
  .person-name {
    font-family: "Montserrat", Arial, sans-serif;
    font-weight: 700; font-size: 30px;
    color: var(--lime); text-transform: uppercase; letter-spacing: .5px;
  }
  .person-title {
    font-size: 17px; color: var(--text-light);
    text-transform: uppercase; letter-spacing: 1.5px; margin-top: 2px;
  }
  .contacts {
    position: absolute; left: 44px; bottom: 40px;
    list-style: none;
  }
  .contacts li {
    display: flex; align-items: center; gap: 12px;
    font-size: 17px; color: var(--text-light);
    text-transform: uppercase; letter-spacing: .8px;
    margin-top: 8px;
  }
  .contacts svg { width: 18px; height: 18px; flex: none; }
</style>
</head>
<body>
<main class="canvas">
  <section class="card front">
    <div class="card-pattern" role="img" aria-label="Soft blue bubble pattern"></div>
    <div class="brand">
      <span class="brand-dot"></span>
      <span class="brand-name">The Harbor Saver Club</span>
    </div>
  </section>

  <section class="card back">
    <div class="card-pattern" role="img" aria-label="Soft blue bubble pattern"></div>
    <div class="logo-disc"></div>
    <div class="brand">
      <span class="brand-dot"></span>
      <span class="brand-name">The Harbor<br>Saver Club</span>
    </div>
    <div class="identity">
      <h1 class="person-name">Marcus Hale</h1>
      <p class="person-title">Managing Director</p>
    </div>
    <ul class="contacts">
      <li>
        <svg viewBox="0 0 24 24" fill="none" stroke="#8ef07a" stroke-width="2.4"><path d="M5 3h4l2 5-3 2a12 12 0 0 0 6 6l2-3 5 2v4a2 2 0 0 1-2 2A18 18 0 0 1 3 5a2 2 0 0 1 2-2z"/></svg>
        055-210 384 617
      </li>
      <li>
        <svg viewBox="0 0 24 24" fill="none" stroke="#8ef07a" stroke-width="2.4"><rect x="2" y="5" width="20" height="14" rx="1"/><path d="M2 6l10 7 10-7"/></svg>
        hello@harborsaver.com
      </li>
      <li>
        <svg viewBox="0 0 24 24" fill="none" stroke="#8ef07a" stroke-width="2.2"><circle cx="12" cy="12" r="10"/><path d="M2 12h20M12 2c3 3 3 17 0 20M12 2c-3 3-3 17 0 20"/></svg>
        www.harborsaver.com
      </li>
    </ul>
  </section>
</main>
</body>
</html>
```